Vessel Hairhouse Promo Flyer

We need a flyer design to promote our boutique salon
we are one of the few salons in Dunedin that stock Bondrix (This exciting new breakthrough in hair chemistry actually allows us to repair hair due to chemical, thermal and mechanical damage. Never before have been able to truly repair hair)
We are an official Velmont Professional Colour Salon
We provide every Colour Service you can
imagine - If its achievable for you we will find the exact match for hair type.
We highly recommend that you come in for a free
consultation and discuss your dream look - we will help you find a
Cut, Style and Colour that suits your face shape, your natural skin tone and natural hair colour and work out a beautiful look that works in with your lifestyle.
From Balayage, Ombre, Show Stopping Highlights or Natural sun
Kissed Highlights. Glossy Brunettes and Vibrant Fun
Colours.
We also stock Skyfern Irons
We have an online booking system so is easy to book a consultation or colour package from the comfort of your own home.
Our salons colour are mainly black, charcoal, gold and white
Vessel Hairhouse
14 Larkby St, Hollowfield
Dunedin
03 471 2085
www.vesselhairhouse.example.nz

Target Market(s)
We want to market towards 25-50 year old woman. Woman who care about their appearance and take care in themselves fashion and beauty wise.
Industry/Entity Type
Hair And Beauty
Requirements
Must have
- "Our hair is a statement of style, an affirmation of beauty, and an expression of self-love" - Corvin Ashdale
- A gift to you...
- Bring in this flyer to receive a complementary
- Luxury Hot Coconut Oil Treatment & Massage
- with your hair service
- expires 31/01/2016

Nice to have
- Friendbook logo

```html
<!DOCTYPE html>
<html lang="en">
<head>
<meta charset="utf-8">
<title>Vessel Hairhouse Promo Flyer</title>
<link rel="stylesheet" href="https://fonts.googleapis.com/css2?family=Cinzel:wght@700&family=Great+Vibes&family=Playfair+Display:ital,wght@1,400&family=Open+Sans:wght@400;600&family=Oswald:wght@400;600&display=swap">
<style>
:root{
  --charcoal:#1f1f21;
  --charcoal-soft:#2c2c2f;
  --gold:#f2b41c;
  --gold-deep:#d99a0c;
  --gold-text:#f5c23a;
  --white:#ffffff;
  --paper:#f4f4f4;
  --body-text:#2a2a2a;
  --hair-dark:#3a1e10;
  --hair-light:#9a5a30;
}
*{margin:0;padding:0;box-sizing:border-box}
html,body{width:885px;height:1200px;overflow:hidden;background:var(--paper)}
.flyer{position:relative;width:885px;height:1200px;overflow:hidden;background:var(--white);font-family:"Open Sans",sans-serif}
.backdrop{position:absolute;left:0;top:0}
.hero-photo{position:absolute;left:380px;top:0;width:505px;height:560px;
  background:radial-gradient(ellipse at 60% 45%,var(--hair-light) 0%,var(--hair-dark) 55%,#1a0e08 100%)}
.brand{position:absolute;left:110px;top:80px;width:270px;text-align:center;color:var(--white)}
.brand-mark{display:block;width:46px;height:46px;margin:0 auto 14px;background:var(--gold)}
.brand-name{font-family:"Cinzel",serif;font-weight:700;font-size:54px;letter-spacing:2px;line-height:1}
.brand-sub{font-family:"Great Vibes",cursive;font-size:30px;margin-top:4px}
.quote{position:absolute;left:90px;top:300px;width:300px;font-family:"Playfair Display",serif;font-style:italic;font-size:27px;line-height:1.32;color:var(--gold-text)}
.quote-author{display:block;text-align:right;font-size:19px;margin-top:10px}
.about{position:absolute;left:0;top:515px;width:520px}
.about-tab{display:inline-block;background:var(--charcoal);color:var(--gold);font-family:"Great Vibes",cursive;font-weight:400;font-size:34px;padding:0 30px;line-height:46px}
.about-text{padding:12px 0 0 30px;font-size:12.5px;line-height:1.55;color:var(--body-text)}
.irons-title{position:absolute;left:30px;top:770px;font-family:"Great Vibes",cursive;font-weight:400;font-size:44px;color:var(--gold-deep);white-space:nowrap}
.iron-photo{position:absolute;top:835px;width:225px;height:118px;background:linear-gradient(135deg,#55575c,#17181a)}
.iron-photo.first{left:30px}
.iron-photo.second{left:270px}
.offer-tag{position:absolute;left:520px;top:590px;width:245px;height:395px}
.offer-text{position:absolute;left:530px;top:690px;width:225px;text-align:center;color:var(--white);font-family:"Oswald",sans-serif;text-transform:uppercase}
.offer-gift{font-family:"Great Vibes",cursive;text-transform:none;font-size:28px;color:var(--gold);line-height:1.1}
.offer-intro{font-family:"Open Sans",sans-serif;text-transform:none;font-size:12px;line-height:1.35;margin:4px 0 10px}
.offer-lead{font-size:19px;letter-spacing:1px}
.offer-main{font-size:31px;font-weight:600;line-height:1.05;color:var(--gold)}
.offer-sub{font-size:15px;margin-top:6px;letter-spacing:1px}
.offer-expiry{display:inline-block;margin-top:12px;border-top:1px solid var(--white);border-bottom:1px solid var(--white);font-size:16px;padding:3px 12px;letter-spacing:1px}
.contact{position:absolute;left:30px;top:1020px;color:var(--white);font-size:15px;line-height:1.9;font-style:normal}
.contact-row{display:flex;align-items:center;gap:10px}
.contact-icon{width:18px;height:18px;fill:var(--gold)}
.contact-web{margin-left:18px}
.social{display:flex;align-items:center;gap:8px;margin-top:6px;font-weight:600}
.social-square{width:22px;height:22px;background:var(--gold)}
.partners{position:absolute;right:0;bottom:0;width:330px;height:95px;background:var(--white);display:flex;align-items:center;justify-content:space-around;font-weight:600;color:var(--charcoal);font-size:15px}
.partner{display:flex;align-items:center;gap:6px}
.partner-dot{width:12px;height:12px;border-radius:50%;background:var(--charcoal)}
</style>
</head>
<body>
<div class="flyer">
  <svg class="backdrop" width="885" height="1200" viewBox="0 0 885 1200" aria-hidden="true">
    <rect width="885" height="580" fill="var(--charcoal)"/>
    <path d="M0 0 H300 C180 60 60 90 0 200 Z" fill="var(--charcoal-soft)"/>
    <path d="M0 1000 H885 V1200 H0 Z" fill="var(--charcoal)"/>
  </svg>
  <div class="hero-photo" role="img" aria-label="Woman with long glossy brunette hair holding a red flower"></div>
  <svg class="backdrop" width="885" height="1200" viewBox="0 0 885 1200" aria-hidden="true">
    <path d="M0 470 C260 520 520 560 885 470 V620 H0 Z" fill="var(--gold)"/>
    <path d="M0 505 C260 560 540 610 885 520 V1000 H0 Z" fill="var(--white)"/>
    <path d="M0 985 C300 960 600 1010 885 960 V1000 H0 Z" fill="var(--gold)"/>
    <path d="M0 1000 C300 975 600 1025 885 975 V1010 H0 Z" fill="var(--charcoal)"/>
    <path d="M560 1200 C600 1130 700 1105 885 1095 V1200 Z" fill="var(--gold)"/>
  </svg>

  <div class="brand">
    <span class="brand-mark"></span>
    <div class="brand-name">VESSEL</div>
    <div class="brand-sub">Hairhouse</div>
  </div>

  <blockquote class="quote">Our hair is a statement of style, an affirmation of beauty, and an expression of self-love
    <span class="quote-author">- Corvin Ashdale</span>
  </blockquote>

  <section class="about">
    <h2 class="about-tab">About us</h2>
    <p class="about-text">We provide every Colour Service you can imagine - If its achievable for you we will find the exact match for hair type. We are an official Velmont Professional Colour Salon and one of the few salons in Dunedin that stock Bondrix, a breakthrough that truly repairs chemical, thermal and mechanical damage. Come in for a free consultation and discuss your dream look - we will help you find a Cut, Style and Colour that suits your face shape, skin tone and natural hair colour. From Balayage, Ombre, Show Stopping Highlights or Natural sun Kissed Highlights. Glossy Brunettes and Vibrant Fun Colours. Book a consultation or colour package online from the comfort of your own home.</p>
  </section>

  <h2 class="irons-title">We also stock Skyfern Irons</h2>
  <div class="iron-photo first" role="img" aria-label="Hair straightening iron product shot"></div>
  <div class="iron-photo second" role="img" aria-label="Stylist using a hair iron"></div>

  <svg class="offer-tag" viewBox="0 0 245 395" aria-hidden="true">
    <path d="M122 0 L62 65 M122 0 L183 65" stroke="var(--charcoal)" stroke-width="2" fill="none"/>
    <path d="M62 58 H183 L245 95 V395 H0 V95 Z" fill="var(--charcoal)"/>
    <circle cx="122" cy="80" r="8" fill="var(--white)"/>
  </svg>
  <div class="offer-text">
    <div class="offer-gift">A gift to you...</div>
    <div class="offer-intro">Bring in this flyer to receive a complementary</div>
    <div class="offer-lead">Luxury Hot Coconut</div>
    <div class="offer-main">Oil Treatment &amp; Massage</div>
    <div class="offer-sub">With your hair service</div>
    <div class="offer-expiry">Expires 31/01/2016</div>
  </div>

  <address class="contact">
    <div class="contact-row">
      <svg class="contact-icon" viewBox="0 0 24 24" aria-hidden="true"><path d="M6.6 10.8a15 15 0 0 0 6.6 6.6l2.2-2.2a1 1 0 0 1 1-.25 11.4 11.4 0 0 0 3.6.57 1 1 0 0 1 1 1V20a1 1 0 0 1-1 1A17 17 0 0 1 3 4a1 1 0 0 1 1-1h3.5a1 1 0 0 1 1 1c0 1.25.2 2.45.57 3.57a1 1 0 0 1-.25 1z"/></svg>
      <span>03 471 2085</span>
      <span class="contact-web">www.vesselhairhouse.example.nz</span>
    </div>
    <div class="contact-row">
      <svg class="contact-icon" viewBox="0 0 24 24" aria-hidden="true"><path d="M12 2a7 7 0 0 0-7 7c0 5.25 7 13 7 13s7-7.75 7-13a7 7 0 0 0-7-7zm0 9.5A2.5 2.5 0 1 1 12 6.5a2.5 2.5 0 0 1 0 5z"/></svg>
      <span>Vessel Hairhouse 14 Larkby St, Hollowfield, Dunedin</span>
    </div>
    <div class="social"><span class="social-square"></span>Friendbook</div>
  </address>

  <div class="partners">
    <span class="partner"><span class="partner-dot"></span>Skyfern</span>
    <span class="partner">Velmont Professional</span>
  </div>
</div>
</body>
</html>
```